Business Card Design Project

restaurant management company needs business card design.

Industry/Entity Type

Restaurant

Requirements
Must have
• our logo
bagel barn logo
RLD logo
WrapDome Logo
Nice to have
• Norris Pelham
(position)

362 Avery Street
Woodstock NB,
Canada
K2R 8H3

Tel 506-xxx-xxxx Ext 201
Fax 506-xxx-xxxx
Mobile 506-xxx-xxxx

norrispelham@tqvgroup.ca
Should not have
• Norris Pelham
(position)

362 Avery Street
Woodstock NB,
Canada
K2R 8H3

Tel 506-xxx-xxxx Ext 201
Fax 506-xxx-xxxx
Mobile 506-xxx-xxxx

norrispelham@tqvgroup.ca

```html
<!DOCTYPE html>
<html lang="en">
<head>
<meta charset="utf-8">
<title>TQV Business Card</title>
<link rel="stylesheet" href="https://fonts.googleapis.com/css2?family=Source+Sans+3:wght@400;600;700&display=swap">
<style>
  :root {
    --backdrop: #eeeee8;
    --card-black: #000000;
    --card-white: #ffffff;
    --accent-red: #e5141b;
    --text-light: #ffffff;
    --ink: #111111;
  }
  html, body {
    margin: 0;
    width: 1200px;
    height: 900px;
    overflow: hidden;
    background: var(--backdrop);
    font-family: "Source Sans 3", sans-serif;
  }
  .card {
    position: absolute;
    left: 180px;
    top: 210px;
    width: 840px;
    height: 480px;
    border-radius: 32px;
    overflow: hidden;
    background: var(--card-black);
  }
  .card-shapes {
    position: absolute;
    inset: 0;
  }
  .contact {
    position: absolute;
    left: 56px;
    top: 0;
    color: var(--text-light);
    font-size: 24px;
    line-height: 1;
  }
  .contact-row {
    position: absolute;
    left: 0;
    white-space: nowrap;
  }
  .contact-label {
    display: inline-block;
    width: 64px;
    color: var(--accent-red);
    font-weight: 600;
    font-size: 22px;
  }
  .contact-value {
    display: inline-block;
    vertical-align: top;
  }
  .holder {
    position: absolute;
    right: 52px;
    top: 46px;
    text-align: right;
  }
  .holder-name {
    color: var(--text-light);
    font-size: 40px;
    font-weight: 400;
    line-height: 1;
    margin: 0;
  }
  .holder-position {
    color: var(--accent-red);
    font-size: 24px;
    margin: 12px 0 0;
  }
  .company {
    position: absolute;
    left: 540px;
    top: 350px;
    width: 290px;
    display: flex;
    align-items: center;
    justify-content: center;
    gap: 12px;
  }
  .company-mark {
    width: 22px;
    height: 22px;
    border-radius: 50%;
    background: var(--accent-red);
  }
  .company-name {
    margin: 0;
    color: var(--ink);
    font-size: 44px;
    font-weight: 600;
    line-height: 1;
    white-space: nowrap;
  }
  .partners {
    position: absolute;
    left: 24px;
    top: 356px;
    width: 440px;
    height: 100px;
    display: flex;
    align-items: center;
    justify-content: space-around;
  }
  .partner {
    display: flex;
    align-items: center;
    gap: 8px;
    color: var(--ink);
    font-weight: 700;
    font-size: 24px;
    white-space: nowrap;
  }
  .partner-dot {
    width: 14px;
    height: 14px;
    border-radius: 50%;
    background: var(--accent-red);
  }
</style>
</head>
<body>
  <div class="card">
    <svg class="card-shapes" width="840" height="480" viewBox="0 0 840 480" aria-hidden="true">
      <rect class="lower-band" x="0" y="326" width="840" height="154" fill="var(--card-white)"/>
      <circle class="brand-disc" cx="740" cy="430" r="280" fill="var(--card-white)"/>
    </svg>

    <div class="contact">
      <div class="contact-row" style="top:62px"><span class="contact-label">tel</span><span class="contact-value">506.555.0142 ext 201</span></div>
      <div class="contact-row" style="top:94px"><span class="contact-label">fax</span><span class="contact-value">506.555.0178</span></div>
      <div class="contact-row" style="top:126px"><span class="contact-label">cel</span><span class="contact-value">506.555.0193</span></div>
      <div class="contact-row" style="top:182px"><span class="contact-label">mail</span><span class="contact-value">norrispelham@tqvgroup.ca</span></div>
      <div class="contact-row" style="top:240px"><span class="contact-label">add</span><span class="contact-value">362 Avery Street, Woodstock<br>NB K2R 8H3, Canada</span></div>
    </div>

    <div class="holder">
      <p class="holder-name">Norris Pelham</p>
      <p class="holder-position">Position</p>
    </div>

    <div class="company">
      <span class="company-mark"></span>
      <p class="company-name">TQV Group</p>
    </div>

    <div class="partners">
      <div class="partner"><span class="partner-dot"></span>RLD</div>
      <div class="partner">bagel barn</div>
      <div class="partner">WrapDome</div>
    </div>
  </div>
</body>
</html>
```